Business Card For Life Coaching Business For Men

Take my existing logo and apply it to a business card. I would like the logo to be prominent with stylistic text below reading Life Coaching For Men. Contact info should show as:
Dale Hartwig
dale@steadforgepath.com

```html
<!DOCTYPE html>
<html lang="en">
<head>
<meta charset="utf-8">
<title>Steadforge Path – Business Card</title>
<link rel="stylesheet" href="https://fonts.googleapis.com/css2?family=Saira+Extra+Condensed:wght@600;700&family=Montserrat:ital,wght@1,600&display=swap">
<style>
  :root {
    --navy: #0b0a8a;
    --teal: #00817f;
    --slate: #7494b5;
    --white: #ffffff;
    --page: #ffffff;
  }
  * { box-sizing: border-box; margin: 0; padding: 0; }
  html, body {
    width: 713px; height: 1200px; overflow: hidden;
    background: var(--page);
  }
  .canvas { position: relative; width: 713px; height: 1200px; }
  .card {
    position: absolute; left: 150px; width: 414px; height: 237px;
    background: var(--white); overflow: hidden;
    box-shadow: 2px 3px 6px rgba(0,0,0,0.25);
  }
  .card--front { top: 320px; }
  .card--back { top: 640px; }
  .card-art { position: absolute; inset: 0; width: 414px; height: 237px; }

  .display {
    font-family: "Saira Extra Condensed", "Arial Narrow", sans-serif;
    font-weight: 700;
    text-transform: uppercase;
  }
  .brand-name { fill: var(--navy); font-size: 60px; }
  .tagline { fill: var(--white); font-size: 26px; font-weight: 600; font-style: italic; letter-spacing: 1px; }
  .person-name { fill: var(--teal); font-size: 44px; }

  .brand-mark { fill: var(--slate); }
  .band { fill: var(--teal); }

  .email-band {
    position: absolute; left: 0; top: 210px; width: 238px; height: 27px;
    background: var(--teal);
    clip-path: polygon(0 0, 100% 0, calc(100% - 6px) 100%, 0 100%);
    display: flex; align-items: center; gap: 5px; padding-left: 8px;
  }
  .email-icon { width: 17px; height: 13px; flex: none; }
  .email {
    font-family: "Montserrat", sans-serif; font-weight: 600; font-style: italic;
    font-size: 11px; color: var(--white); white-space: nowrap;
  }
</style>
</head>
<body>
<main class="canvas">
  <section class="card card--front">
    <svg class="card-art" viewBox="0 0 414 237">
      <circle class="brand-mark" cx="100" cy="120" r="72"/>
      <text class="display brand-name" x="204" y="113" textLength="146" lengthAdjust="spacingAndGlyphs">Steadforge</text>
      <text class="display brand-name" x="204" y="160" textLength="68" lengthAdjust="spacingAndGlyphs">Path</text>
      <polygon class="band" points="156,181 414,181 414,209 142,209"/>
      <text class="display tagline" x="182" y="204" textLength="204" lengthAdjust="spacingAndGlyphs">Life Coaching For Men</text>
    </svg>
  </section>

  <section class="card card--back">
    <svg class="card-art" viewBox="0 0 414 237">
      <circle class="brand-mark" cx="318" cy="140" r="96"/>
      <rect class="band" x="0" y="120" width="14" height="49"/>
      <text class="display person-name" x="26" y="144" textLength="56" lengthAdjust="spacingAndGlyphs">Dale</text>
      <text class="display person-name" x="26" y="182" textLength="97" lengthAdjust="spacingAndGlyphs">Hartwig</text>
    </svg>
    <div class="email-band">
      <svg class="email-icon" viewBox="0 0 17 13" aria-hidden="true">
        <rect x="0" y="0" width="17" height="13" rx="1" fill="#ffffff"/>
        <polyline points="1,1.5 8.5,7.5 16,1.5" fill="none" stroke="#00817f" stroke-width="1.8"/>
      </svg>
      <span class="email">dale@steadforgepath.com</span>
    </div>
  </section>
</main>
</body>
</html>
```